integrative health clinic-Medical massage, acupuncture, chiropractic

we like our logo, but are open to new ideas. We need a new card design. We have added chiropractic and acupuncture that we have put under the name of the business. We are an integrative medical clinic

Target Market(s)

General public, athletes

Contact Information for Business Card

Phone 5055583927
Fax 5055583926
Hours Monday-Friday 9-6
Saturday 10-6
The 20% can be smaller on the back

Colors
3176b5
0355a3

Requirements
Must have
• Logo but am open to ideas
Nice to have
• We are an integrated medical clinic but also want to be personable. We want the card fun and inviting

```html
<!DOCTYPE html>
<html lang="en">
<head>
<meta charset="utf-8">
<title>Full Motion Wellness – Business Card</title>
<link rel="stylesheet" href="https://fonts.googleapis.com/css2?family=Encode+Sans+Semi+Condensed:wght@600&family=Jost:wght@500&family=Source+Sans+3:wght@300;400&display=swap">
<style>
  :root {
    --stage: #0a1428;
    --card-navy: #0d1630;
    --card-deep: #0a1024;
    --band-blue: #1a3566;
    --band-edge: #0f1f45;
    --gold: #c6a66c;
    --gold-light: #e6d29c;
    --text-cream: #e9dcb8;
    --figure-tone: #a9a779;
    --figure-shadow: #3b3d2e;
  }
  * { margin: 0; padding: 0; box-sizing: border-box; }
  html, body {
    width: 1200px; height: 900px; overflow: hidden;
    background: var(--stage);
  }
  .stage {
    position: relative; width: 1200px; height: 900px;
    background: radial-gradient(ellipse at 50% 40%, #13213f 0%, var(--stage) 75%);
  }
  .card {
    position: absolute; left: 230px; width: 740px; height: 410px;
    background: linear-gradient(160deg, var(--card-navy) 0%, var(--card-deep) 100%);
    overflow: hidden;
    box-shadow: 0 14px 40px rgba(0,0,0,0.6);
  }
  .card--front { top: 30px; }
  .card--back { top: 465px; }
  .card__lines { position: absolute; inset: 0; width: 100%; height: 100%; }

  .figure-art {
    position: absolute; left: 0; top: 70px; width: 260px; height: 320px;
    background: radial-gradient(ellipse 60% 55% at 50% 50%, var(--figure-tone) 0%, #6f7052 45%, rgba(59,61,46,0.5) 75%, transparent 100%);
    opacity: 0.85;
  }

  .brand-name {
    font-family: "Encode Sans Semi Condensed", "Arial Narrow", sans-serif;
    font-weight: 600; color: var(--gold);
    letter-spacing: -0.5px; line-height: 1; white-space: nowrap;
  }
  .brand-mark {
    position: absolute; border-radius: 50%; background: var(--gold);
  }
  .tagline {
    font-family: "Source Sans 3", "Segoe UI", sans-serif;
    font-weight: 300; color: var(--gold); white-space: nowrap; line-height: 1;
  }
  .services {
    font-family: "Jost", "Futura", sans-serif; font-weight: 500;
    color: var(--text-cream); text-align: center; letter-spacing: 2px; line-height: 1.3;
    white-space: nowrap;
  }

  /* front */
  .card--front .brand-name { position: absolute; left: 285px; top: 88px; font-size: 48px; }
  .card--front .brand-mark { left: 290px; top: 152px; width: 24px; height: 24px; }
  .card--front .tagline { position: absolute; left: 328px; top: 151px; font-size: 24px; }
  .card--front .services { position: absolute; left: 280px; width: 440px; top: 200px; font-size: 13px; }

  /* back */
  .info-band {
    position: absolute; left: 0; right: 0; top: 268px; height: 102px;
    background: linear-gradient(180deg, var(--band-blue) 0%, var(--band-edge) 100%);
  }
  .card--back .brand-name { position: absolute; left: 60px; top: 44px; font-size: 72px; }
  .card--back .brand-mark { left: 64px; top: 134px; width: 40px; height: 40px; }
  .card--back .tagline { position: absolute; left: 130px; top: 132px; font-size: 38px; }
  .card--back .services { position: absolute; left: 150px; width: 560px; top: 196px; font-size: 15px; }

  .person { position: absolute; left: 60px; top: 282px; }
  .person__name {
    font-family: "Jost", "Futura", sans-serif; font-weight: 500;
    font-size: 32px; letter-spacing: 5px; color: var(--text-cream); line-height: 1;
  }
  .person__role {
    font-family: "Source Sans 3", "Segoe UI", sans-serif; font-weight: 400;
    font-size: 20px; color: var(--text-cream); margin-top: 6px; padding-left: 28px;
  }
  .contact {
    position: absolute; left: 320px; top: 290px;
    font-family: "Source Sans 3", "Segoe UI", sans-serif; font-size: 18px; color: var(--text-cream);
  }
  .contact__row { display: flex; align-items: center; gap: 10px; height: 32px; }
  .contact__icon { width: 22px; height: 22px; }
  .hours {
    position: absolute; left: 520px; top: 296px;
    font-family: "Source Sans 3", "Segoe UI", sans-serif; font-size: 17px; color: var(--text-cream); line-height: 1.85;
  }
  .promo {
    position: absolute; left: 300px; top: 372px;
    font-family: "Jost", "Futura", sans-serif; font-weight: 500;
    font-size: 16px; letter-spacing: 3px; color: var(--text-cream); white-space: nowrap;
  }
</style>
</head>
<body>
<main class="stage">

  <section class="card card--front">
    <svg class="card__lines" viewBox="0 0 740 410" preserveAspectRatio="none" aria-hidden="true">
      <path d="M0 6 C 250 22, 500 36, 740 60 L740 0 L0 0 Z" fill="#0a1226"/>
      <path d="M0 6 C 250 22, 500 36, 740 60" fill="none" stroke="var(--gold-light)" stroke-width="2"/>
      <path d="M0 372 C 250 376, 500 390, 740 410 L740 410 L0 410 Z" fill="var(--band-blue)"/>
      <path d="M0 372 C 250 376, 500 390, 740 410" fill="none" stroke="var(--gold)" stroke-width="2"/>
    </svg>
    <div class="figure-art" role="img" aria-label="Illustration of a crouching runner with visible skeleton and glowing joint pain points"></div>
    <div class="brand-name">Full Motion Wellness</div>
    <span class="brand-mark"></span>
    <div class="tagline">Sports Therapy and Wellness Center</div>
    <p class="services">Specializing in<br>Medical, Sports Massage and Manual Therapies<br>Acupuncture Chiropratic with Bullet Point</p>
  </section>

  <section class="card card--back">
    <svg class="card__lines" viewBox="0 0 740 410" preserveAspectRatio="none" aria-hidden="true">
      <path d="M0 5 C 250 14, 500 22, 740 32" fill="none" stroke="var(--gold-light)" stroke-width="2"/>
      <path d="M0 395 C 250 398, 500 402, 740 404" fill="none" stroke="var(--gold-light)" stroke-width="3"/>
    </svg>
    <div class="info-band"></div>
    <div class="brand-name">Full Motion Wellness</div>
    <span class="brand-mark"></span>
    <div class="tagline">Sports Therapy and Wellness Center</div>
    <p class="services">Specializing in<br>Medical, Sports Massage and Manual Therapies<br>Acupuncture Chiropratic with Bullet Point</p>

    <div class="person">
      <div class="person__name">Your Name</div>
      <div class="person__role">Pain Specialist</div>
    </div>

    <div class="contact">
      <div class="contact__row">
        <svg class="contact__icon" viewBox="0 0 24 24" aria-label="Phone">
          <circle cx="12" cy="12" r="11" fill="none" stroke="var(--text-cream)" stroke-width="1.5"/>
          <path d="M8 6.5 l2 -0.5 1.2 3 -1.4 1 a6 6 0 0 0 3.2 3.2 l1 -1.4 3 1.2 -0.5 2 c-5 0.5 -9 -3.5 -8.5 -8.5 z" fill="var(--text-cream)"/>
        </svg>
        <span>5055583927</span>
      </div>
      <div class="contact__row">
        <svg class="contact__icon" viewBox="0 0 24 24" aria-label="Fax">
          <circle cx="12" cy="12" r="11" fill="none" stroke="var(--text-cream)" stroke-width="1.5"/>
          <rect x="6" y="8" width="12" height="8" fill="var(--text-cream)"/>
          <path d="M6 8 l6 5 6 -5" fill="none" stroke="var(--card-navy)" stroke-width="1.2"/>
        </svg>
        <span>5055583926</span>
      </div>
    </div>

    <div class="hours">Hours Monday-Friday 9-6<br>Saturday 10-6</div>
    <p class="promo">The 20% can be smaller on the back</p>
  </section>

</main>
</body>
</html>
```